Torvane PT Business Card

I need the card to be bright/bold colours to stand out amongst others.
It needs to have my company logo.
I was not interested in pictures etc just a layout that attracts attention.

I have attached my old design which is very plain. I also needed change the contact details. And my description changed to Personal Trainer
Phone 0427391058
Facebook Torvane PT
No email address please, no street address.
And only Torvane PT (Please remove anything to do with Torvane Supplements)

```html
<!DOCTYPE html>
<html lang="en">
<head>
<meta charset="UTF-8">
<title>Torvane PT Business Card</title>
<link rel="stylesheet" href="https://fonts.googleapis.com/css2?family=Open+Sans:wght@400;700;800&display=swap">
<style>
  :root {
    --stage: #666666;
    --card-white: #ffffff;
    --brand-blue: #0a87c9;
    --ink: #3a3a3a;
    --on-blue: #ffffff;
  }
  * { margin: 0; padding: 0; box-sizing: border-box; }
  html, body {
    width: 1200px;
    height: 900px;
    overflow: hidden;
    background: var(--stage);
    font-family: "Open Sans", Arial, sans-serif;
  }
  .canvas { position: relative; width: 1200px; height: 900px; }
  .card {
    position: absolute;
    top: 271px;
    width: 457px;
    height: 281px;
    border-radius: 14px;
  }
  .card-front { left: 137px; background: var(--card-white); }
  .card-back { left: 626px; background: var(--brand-blue); }

  .brand-name {
    position: absolute;
    right: 25px;
    top: 28px;
    font-weight: 800;
    font-size: 34px;
    letter-spacing: 1px;
    color: var(--brand-blue);
    line-height: 1;
  }
  .holder-name {
    position: absolute;
    right: 25px;
    top: 132px;
    font-weight: 700;
    font-size: 18px;
    color: var(--brand-blue);
    letter-spacing: 0.3px;
    line-height: 24px;
  }
  .holder-rule {
    position: absolute;
    left: 27px;
    top: 163px;
    width: 283px;
    height: 2px;
    background: var(--brand-blue);
  }
  .holder-role {
    position: absolute;
    right: 25px;
    top: 155px;
    font-size: 12px;
    color: var(--ink);
    line-height: 17px;
  }
  .contact-list {
    position: absolute;
    left: 27px;
    top: 180px;
    list-style: none;
    font-size: 12.5px;
    color: var(--ink);
  }
  .contact-list li {
    display: flex;
    align-items: center;
    height: 16.5px;
  }
  .contact-icon { width: 9px; height: 9px; margin-right: 7px; flex: none; }
  .contact-icon-square { background: var(--brand-blue); border-radius: 1.5px; }

  .back-brand {
    position: absolute;
    left: 0;
    right: 0;
    top: 113px;
    text-align: center;
    font-weight: 800;
    color: var(--on-blue);
    line-height: 1;
  }
  .back-brand-main { display: block; font-size: 40px; letter-spacing: 1px; }
  .back-brand-sub { display: block; font-size: 14px; letter-spacing: 7px; margin-top: 3px; padding-left: 7px; }
</style>
</head>
<body>
<main class="canvas">
  <section class="card card-front" aria-label="Business card front">
    <div class="brand-name">TORVANE PT</div>
    <div class="holder-name">JORDAN HALE</div>
    <div class="holder-rule"></div>
    <div class="holder-role">PERSONAL TRAINER</div>
    <ul class="contact-list">
      <li>
        <svg class="contact-icon" viewBox="0 0 10 10" aria-hidden="true">
          <path d="M1 4 Q5 1 9 4 L8 5 L6.5 4 L6.5 3.3 Q5 2.9 3.5 3.3 L3.5 4 L2 5 Z M2.5 5.5 H7.5 L8.5 9 H1.5 Z" fill="#0a87c9"/>
        </svg>
        0427391058
      </li>
      <li><span class="contact-icon contact-icon-square"></span>Torvane PT</li>
    </ul>
  </section>

  <section class="card card-back" aria-label="Business card back">
    <div class="back-brand">
      <span class="back-brand-main">TORVANE</span>
      <span class="back-brand-sub">PT</span>
    </div>
  </section>
</main>
</body>
</html>
```